Coffee Package Design

We need a new package design for a coffee company. Need to be a mix between modern and classic design combined together. We are open to different ideas.
We changing our product name from Café Verlona to Café Rostelli. The picture upload
shows what the product looks like. We want something completely different. The name of the company should go on the back of the package.
Updates

Hello Everyone,

Please read description, we are going with a new name and design for the product.

Café Rostelli. Café Verlona is what we are replacing with Café Rostelli, we are looking for new

look and design, please submit new designs.

There is a change in the description. Please take out Premium coffee blend and replace with Italian Roast.                                    

Industry/Entity Type

Cafe

Requirements
Must have
• You can use up to 6 colors.
Please put these items on design: Café Rostelli (this is the product name), Regular Premium Blend Coffee, 100% Arabica,
Dumbrell & Sons (name of the company), Tyler, TX on the back of the package

The file uploaded is an example of one of our products and how the package film
is sized.

```html
<!DOCTYPE html>
<html lang="en">
<head>
<meta charset="utf-8">
<title>Café Rostelli – Italian Roast Package</title>
<link rel="stylesheet" href="https://fonts.googleapis.com/css2?family=Oxygen:wght@300;400&family=Roboto+Condensed:wght@400;700&family=Roboto:wght@400&display=swap">
<style>
  :root {
    --backdrop: #3b3b3b;
    --film: #1f1c1a;
    --seal-band: #8a8461;
    --seal-band-dark: #6f6a4c;
    --teal: #2a9d8a;
    --teal-deep: #1d6f63;
    --cream: #ebe6cf;
    --muted: #9c978a;
  }
  html, body {
    margin: 0;
    padding: 0;
    width: 1200px;
    height: 960px;
    overflow: hidden;
    background: var(--backdrop);
  }
  .canvas {
    position: relative;
    width: 1200px;
    height: 960px;
  }
  .package-film {
    position: absolute;
    left: 0;
    top: 0;
  }
  .label {
    position: absolute;
    left: 330px;
    width: 540px;
    text-align: center;
    margin: 0;
    line-height: 1.2;
    white-space: nowrap;
  }
  .company-name {
    top: 254px;
    font-family: "Roboto Condensed", sans-serif;
    font-weight: 700;
    font-size: 22px;
    color: var(--cream);
    letter-spacing: 0.5px;
  }
  .company-town {
    top: 285px;
    font-family: "Roboto", sans-serif;
    font-size: 11px;
    color: var(--muted);
    letter-spacing: 0.3px;
  }
  .product-prefix {
    top: 370px;
    font-family: "Oxygen", sans-serif;
    font-weight: 400;
    font-size: 34px;
    color: var(--cream);
  }
  .product-name {
    top: 412px;
    font-family: "Oxygen", sans-serif;
    font-weight: 300;
    font-size: 74px;
    line-height: 1;
    color: var(--cream);
  }
  .roast-origin {
    top: 588px;
    font-family: "Roboto", sans-serif;
    font-size: 29px;
    color: var(--cream);
    letter-spacing: 2px;
  }
  .roast-type {
    top: 626px;
    font-family: "Roboto Condensed", sans-serif;
    font-size: 21px;
    color: var(--muted);
  }
  .blend-strength {
    top: 662px;
    font-family: "Roboto Condensed", sans-serif;
    font-weight: 700;
    font-size: 32px;
    color: var(--teal);
    letter-spacing: 0.5px;
  }
  .bean-type {
    top: 706px;
    font-family: "Roboto", sans-serif;
    font-size: 16px;
    color: var(--cream);
  }
</style>
</head>
<body>
<main class="canvas">
  <svg class="package-film" width="1200" height="960" viewBox="0 0 1200 960">
    <defs>
      <pattern id="teeth-top" width="10" height="8" patternUnits="userSpaceOnUse" x="330" y="122">
        <path d="M0 8 L5 0 L10 8 Z" fill="var(--seal-band)"/>
      </pattern>
      <pattern id="teeth-bottom" width="10" height="8" patternUnits="userSpaceOnUse" x="330" y="830">
        <path d="M0 0 L5 8 L10 0 Z" fill="var(--seal-band)"/>
      </pattern>
      <linearGradient id="frame-tone" x1="0" y1="0" x2="1" y2="1">
        <stop offset="0" stop-color="var(--teal)"/>
        <stop offset="1" stop-color="var(--teal-deep)"/>
      </linearGradient>
    </defs>

    <rect class="pouch-body" x="330" y="130" width="540" height="700" fill="var(--film)"/>

    <rect x="330" y="122" width="540" height="8" fill="url(#teeth-top)"/>
    <rect class="seal-band" x="330" y="130" width="540" height="50" fill="var(--seal-band)"
          role="img" aria-label="Decorative patterned seal band"/>
    <rect class="hang-slot" x="568" y="147" width="64" height="14" rx="7" fill="none" stroke="var(--seal-band-dark)" stroke-width="2"/>

    <rect class="seal-band" x="330" y="772" width="540" height="58" fill="var(--seal-band)"
          role="img" aria-label="Decorative patterned seal band"/>
    <rect x="330" y="830" width="540" height="8" fill="url(#teeth-bottom)"/>

    <rect class="flourish" x="540" y="228" width="120" height="14" rx="7" fill="var(--muted)" opacity="0.55"
          role="img" aria-label="Small calligraphic flourish"/>

    <rect class="name-frame" x="400" y="318" width="400" height="250" rx="70" fill="url(#frame-tone)"
          role="img" aria-label="Ornate baroque scroll frame around the product name"/>
    <rect class="name-panel" x="432" y="346" width="336" height="194" rx="46" fill="var(--film)"/>

    <polygon class="ribbon-end" points="492,671 516,671 516,693 492,693 499,682" fill="var(--teal)"/>
    <polygon class="ribbon-end" points="708,671 684,671 684,693 708,693 701,682" fill="var(--teal)"/>
  </svg>

  <p class="label company-name">DUMBRELL &amp; SONS</p>
  <p class="label company-town">MARBECK, TEXAS</p>
  <p class="label product-prefix">Café</p>
  <p class="label product-name">Rostelli</p>
  <p class="label roast-origin">Italian</p>
  <p class="label roast-type">Roast</p>
  <p class="label blend-strength">REGULAR</p>
  <p class="label bean-type">100% ARABICA</p>
</main>
</body>
</html>
```